Food Safety 1-California workers only

3.25" by 4.5" Black and White Magazine Ad
This ad is to train California workers only.
Workers will be trained on: Food Safety, FSMA (Food Safety Modernization Act), using equipment safety, food processing production skills, worker safety, supervisory skills, communication skills.
"FREE TRAINING", The company does the training or Keystone Learning will provide the training.
Training grants range from $100,000 to $400,000.
Companies must be in business for profit.
Companies must train 200 employees or more.
This program is for California workers only.
Incumbent or new-hires are eligible.

Target Market(s)

California food processors, farms, food packaging, food processors, companies under FSMA, food safety, food production who need to train employees.

Industry/Entity Type

Food Production

Font styles to use
Serif
Sans Serif

Colors

Designer to choose colors to be used in the design.

Requirements
Must have
• This is a 3.25 inch by 4.5 inch magazine ad. It must be black and white. No color.
• The deliverable must be in basic PhotoShop. The ad does not need to include any graphics and be text only if needed. If you have a black and white graphic that will show well.
• Look at www.KLGFoodSafety..com
• Use the text from "MEALBOX-Photoshop-052018" file as your starting point.
Nice to have
• A black and white graphic about food. See www.KLGFoodSafety.com
Should not have
• No color.

```html
<!DOCTYPE html>
<html lang="en">
<head>
<meta charset="utf-8">
<title>Free Training Ad</title>
<link rel="stylesheet" href="https://fonts.googleapis.com/css2?family=Playfair+Display:wght@700;900&family=Open+Sans:wght@600;700&family=Barlow+Condensed:wght@300;400;600;700&display=swap">
<style>
:root{
  --mat:#d1d2d4;
  --paper:#ffffff;
  --ink:#111111;
  --text:#1e1e1e;
  --quote:#2b2b2b;
  --photo-light:#bdbdbd;
  --photo-dark:#6b6b6b;
}
*{margin:0;padding:0;box-sizing:border-box}
html,body{width:1045px;height:1200px;overflow:hidden;background:var(--mat)}
.canvas{position:relative;width:1045px;height:1200px}
.ad{position:absolute;left:146px;top:97px;width:729px;height:1008px;background:var(--paper);border:5px solid var(--ink)}
.ad-inner-rule{position:absolute;left:1px;top:1px;right:1px;bottom:1px;border:1.5px solid var(--ink)}
.hero-photo{position:absolute;left:6px;top:5px;width:705px;height:448px;
  background:radial-gradient(ellipse at 70% 30%,#e4e4e4 0%,var(--photo-light) 45%,var(--photo-dark) 100%)}
.headline{position:absolute;left:0;width:100%;text-align:center;font-family:"Playfair Display",serif;font-weight:900;color:#fff;
  text-shadow:3px 3px 0 #333,-1px -1px 0 #333,1px -1px 0 #333,-1px 1px 0 #333;letter-spacing:2px;line-height:1;white-space:nowrap}
.headline-free{top:84px;font-size:76px}
.headline-training{top:152px;font-size:80px}
.quote-box{position:absolute;left:147px;top:236px;width:424px;height:77px;background:rgba(255,255,255,.82);
  font-family:"Open Sans",sans-serif;font-weight:600;font-size:24px;line-height:32px;color:var(--quote);text-align:center;padding-top:7px;white-space:nowrap}
.badge{position:absolute;left:256px;top:350px;width:206px;height:103px;border-radius:103px 103px 0 0;background:var(--paper)}
.food-graphic{position:absolute;left:276px;top:360px;width:166px;height:120px;border-radius:50% 50% 40% 40%;
  background:radial-gradient(ellipse at 50% 55%,#8a8a8a 0%,#c9c9c9 55%,rgba(255,255,255,0) 72%)}
.topics{position:absolute;left:41px;top:503px;width:642px;height:54px;border-top:1px solid var(--ink);border-bottom:1px solid var(--ink);
  font-family:"Barlow Condensed",sans-serif;font-weight:700;font-size:29px;color:var(--ink);text-align:center;line-height:52px;white-space:nowrap;overflow:hidden}
.qualify-title{position:absolute;left:0;top:595px;width:100%;text-align:center;font-family:"Open Sans",sans-serif;font-weight:700;font-size:27px;color:var(--ink)}
.criteria{position:absolute;list-style:none;font-family:"Barlow Condensed",sans-serif;font-weight:400;font-size:23px;line-height:26px;color:var(--text)}
.criteria li{position:relative;padding-left:30px;margin-bottom:13px;white-space:nowrap}
.criteria svg{position:absolute;left:0;top:5px;width:17px;height:17px}
.criteria-left{left:55px;top:654px;width:300px}
.criteria-right{left:388px;top:654px;width:320px}
.contact-band{position:absolute;left:4px;top:862px;width:711px;height:132px;background:var(--ink);color:#fff;
  font-family:"Barlow Condensed",sans-serif;font-weight:400;font-size:22px;text-align:center;padding-top:15px;line-height:36px;white-space:nowrap}
.contact-band svg{width:15px;height:15px;vertical-align:-2px;fill:#fff}
</style>
</head>
<body>
<div class="canvas">
  <div class="ad">
    <div class="ad-inner-rule"></div>
    <div class="hero-photo" role="img" aria-label="Black and white photo of a head chef showing a group of kitchen trainees a cutting technique"></div>
    <div class="headline headline-free">FREE</div>
    <div class="headline headline-training">TRAINING</div>
    <div class="quote-box">“WE DO THE TRAINING AND<br>THE STATE PAYS FOR IT!”</div>
    <div class="badge"></div>
    <div class="food-graphic" role="img" aria-label="Safety cone surrounded by bread, pears, grapes and sweet potatoes"></div>

    <div class="topics">FOOD SAFETY • FSMA • PRODUCTION SKILLS • WORKER SAFETY</div>

    <h2 class="qualify-title">HOW TO QUALIFY:</h2>

    <ul class="criteria criteria-left">
      <li><svg viewBox="0 0 17 17"><rect x="1" y="3" width="13" height="13" fill="none" stroke="#111" stroke-width="1.6"/><path d="M4 9l3 3 8-9" fill="none" stroke="#111" stroke-width="1.8"/></svg>Train California Workers Only</li>
      <li><svg viewBox="0 0 17 17"><rect x="1" y="3" width="13" height="13" fill="none" stroke="#111" stroke-width="1.6"/><path d="M4 9l3 3 8-9" fill="none" stroke="#111" stroke-width="1.8"/></svg>Trainees must earn $11/hour</li>
      <li><svg viewBox="0 0 17 17"><rect x="1" y="3" width="13" height="13" fill="none" stroke="#111" stroke-width="1.6"/><path d="M4 9l3 3 8-9" fill="none" stroke="#111" stroke-width="1.8"/></svg>Full-time workers only</li>
      <li><svg viewBox="0 0 17 17"><rect x="1" y="3" width="13" height="13" fill="none" stroke="#111" stroke-width="1.6"/><path d="M4 9l3 3 8-9" fill="none" stroke="#111" stroke-width="1.8"/></svg>Employees must attend at<br>least 8 Hours of training</li>
    </ul>

    <ul class="criteria criteria-right">
      <li><svg viewBox="0 0 17 17"><rect x="1" y="3" width="13" height="13" fill="none" stroke="#111" stroke-width="1.6"/><path d="M4 9l3 3 8-9" fill="none" stroke="#111" stroke-width="1.8"/></svg>You must train 200 or more<br>employees</li>
      <li><svg viewBox="0 0 17 17"><rect x="1" y="3" width="13" height="13" fill="none" stroke="#111" stroke-width="1.6"/><path d="M4 9l3 3 8-9" fill="none" stroke="#111" stroke-width="1.8"/></svg>Incumbent or New-Hire workers<br>are eligible</li>
      <li><svg viewBox="0 0 17 17"><rect x="1" y="3" width="13" height="13" fill="none" stroke="#111" stroke-width="1.6"/><path d="M4 9l3 3 8-9" fill="none" stroke="#111" stroke-width="1.8"/></svg>Seasonal workers are eligible</li>
    </ul>

    <div class="contact-band">
      <div>Contact Daniel Porter | Keystone Learning Company, Inc. | <svg viewBox="0 0 16 16"><path d="M3.5 1l2.5 3-1.5 2c1 2 3 4 5 5l2-1.5 3 2.5-1.5 2.5C7 14 2 9 1 2.5z"/></svg> (949) 555-0142</div>
      <div>1200 Harbor Crest Drive, Suite 310, Irvine, CA 92618</div>
      <div>www.KLGCAL.com | www.KLGFoodSafety.com | <svg viewBox="0 0 16 16"><path d="M1 3h14v10H1z M1.5 3.5L8 9l6.5-5.5" fill="#fff" stroke="#111" stroke-width="1"/></svg> Dan.Porter@KLGCAL.com</div>
    </div>
  </div>
</div>
</body>
</html>
```